Qorva Financial's Remote Billing Assistance Descriptive Slicker

We need a flyer (we call them slickers) for one of our products here at Qorva Financial. We had another project manager post this job and we did not really get what we were looking for. I will attach the two versions that we liked the best but do not use them as a template. We would like a completely different direction for this project. If you have any questions or comments whatsoever, please feel free to ask!
Target Market(s)
Healthcare World
Industry/Entity Type
Financial
Requirements
Must have
- Winning design needs to be focused on American healthcare leadership and decision-makers. Sharp, cutting-edge and slick.
Nice to have
- Make sure to remember the Qorva Financial color schemes when creating options (Dark Blue, Burgundy, and Gray).
Should not have
- Please do not use greens or orange colors.

```html
<!DOCTYPE html>
<html lang="en">
<head>
<meta charset="utf-8">
<title>Qorva Financial – Remote Billing Assistance Slicker</title>
<link rel="stylesheet" href="https://fonts.googleapis.com/css2?family=Source+Sans+3:wght@400;600;700&display=swap">
<style>
  :root {
    --navy: #131a33;
    --burgundy: #4a1616;
    --gray: #7b7b80;
    --swatch-gray: #8a8a8f;
    --gray-light: #d4d4d7;
    --paper: #ffffff;
    --stage: #2a2a2c;
  }
  * { box-sizing: border-box; margin: 0; padding: 0; }
  html, body { width: 1200px; height: 900px; overflow: hidden; }
  body {
    background: var(--stage);
    font-family: "Source Sans 3", "Myriad Pro", Arial, sans-serif;
    position: relative;
  }
  .slicker {
    position: absolute;
    left: 290px; top: 25px;
    width: 618px; height: 855px;
    background: var(--paper);
    overflow: hidden;
  }
  .slicker > * { position: absolute; }

  .brand { left: 10px; top: 24px; display: flex; align-items: center; gap: 10px; }
  .brand-mark { width: 34px; height: 34px; background: var(--burgundy); border-radius: 4px; }
  .brand-name { font-size: 33px; font-weight: 600; color: var(--navy); letter-spacing: 0.3px; }

  .rule { height: 2px; background: var(--burgundy); }
  .rule--brand { left: 10px; top: 85px; width: 255px; }
  .rule--mid { left: 43px; top: 447px; width: 385px; }
  .rule--low { left: 43px; top: 610px; width: 385px; }

  .headline { left: 10px; top: 102px; font-size: 24px; font-weight: 700; color: var(--burgundy); }
  .tagline { left: 10px; top: 144px; font-size: 19.5px; color: var(--gray); }
  .lead-in { left: 10px; top: 172px; font-size: 22px; font-weight: 700; color: var(--gray); }

  .services { left: 12px; top: 208px; list-style: none; }
  .services li {
    position: relative; padding-left: 20px;
    font-size: 24px; line-height: 30px; color: var(--burgundy);
  }
  .services li::before {
    content: ""; position: absolute; left: 0; top: 12px;
    width: 11px; height: 11px; border-radius: 50%; background: var(--burgundy);
  }
  .services .wrap { display: inline-block; width: 220px; }

  .benefit { left: 31px; top: 367px; width: 400px; font-size: 18.5px; line-height: 23px; color: var(--gray); }

  .photo { border-radius: 50%; border: 5px solid var(--gray-light); }
  .photo--agents {
    left: 283px; top: -12px; width: 345px; height: 345px;
    background: radial-gradient(circle at 55% 35%, #f4efea 0%, #e6ddd6 35%, #c9c6c8 70%, #9ea3ab 100%);
  }
  .photo--desk {
    left: 445px; top: 262px; width: 166px; height: 166px;
    background: linear-gradient(160deg, #efe3d2, #d9c2a5 50%, #8a7260);
  }

  .tile { top: 458px; height: 142px; border-radius: 4px; }
  .tile--office { left: 22px; width: 194px; background: linear-gradient(160deg, #e6ecf2, #b8c3cf 55%, #5a6478); }
  .tile--meeting { left: 225px; width: 210px; background: linear-gradient(150deg, #f3efea, #d8c9bb 55%, #7a5a4c); }

  .swatches { left: 455px; top: 470px; display: flex; gap: 6px; }
  .swatch { width: 40px; height: 40px; border-radius: 6px; }
  .swatch--navy { background: var(--navy); }
  .swatch--burgundy { background: var(--burgundy); }
  .swatch--gray { background: var(--swatch-gray); }

  .section-title { left: 23px; top: 620px; font-size: 23px; font-weight: 700; color: var(--navy); }
  .how-copy { left: 23px; top: 654px; width: 560px; font-size: 15.3px; line-height: 19.5px; color: var(--gray); }

  .programs { left: 25px; top: 762px; list-style: none; }
  .programs li { position: relative; padding-left: 13px; font-size: 15.5px; line-height: 19.5px; color: var(--burgundy); }
  .programs li::before {
    content: ""; position: absolute; left: 0; top: 7px;
    width: 6px; height: 6px; border-radius: 50%; background: var(--burgundy);
  }

  .cta { right: 35px; top: 758px; text-align: right; color: var(--burgundy); font-weight: 700; line-height: 26px; }
  .cta-line { font-size: 22px; display: flex; align-items: center; justify-content: flex-end; gap: 2px; }
  .cta-icon { width: 21px; height: 21px; fill: var(--burgundy); }
  .cta-phone { font-size: 21px; }

  .footer-line { left: 0; width: 618px; top: 823px; text-align: center; font-size: 15px; color: var(--navy); }
</style>
</head>
<body>
  <article class="slicker">
    <div class="photo photo--agents" role="img" aria-label="Smiling call center agents wearing headsets"></div>
    <div class="photo photo--desk" role="img" aria-label="Agent with headset typing at a desk"></div>

    <div class="brand">
      <span class="brand-mark"></span>
      <span class="brand-name">Qorva Financial</span>
    </div>
    <div class="rule rule--brand"></div>

    <h1 class="headline">Reclaim Your Patient AR</h1>
    <p class="tagline">Not just another letter series!</p>
    <p class="lead-in">Let us:</p>
    <ul class="services">
      <li><span class="wrap">Make the telephone calls</span></li>
      <li>Answer the telephone calls</li>
      <li>Establish payment agreements</li>
      <li>Accept payments</li>
    </ul>
    <p class="benefit">We make notes directly into you’re HIS!&nbsp; Imagine the extra time your team will have to work the insurance claims!</p>

    <div class="rule rule--mid"></div>
    <div class="tile tile--office" role="img" aria-label="Two businessmen reviewing documents"></div>
    <div class="tile tile--meeting" role="img" aria-label="Team meeting around a table with paperwork"></div>
    <div class="swatches" aria-hidden="true">
      <span class="swatch swatch--navy"></span>
      <span class="swatch swatch--burgundy"></span>
      <span class="swatch swatch--gray"></span>
    </div>
    <div class="rule rule--low"></div>

    <h2 class="section-title">How it Works</h2>
    <p class="how-copy">You set the parameters. We utilize a combination of call center agents and remote billing support.&nbsp; We log in to your billing system each day and work your accounts as if we were sitting in the office next to you. By strategically placing remote billing agents throughout the U.S., we help you to maximize your efficiencies and reduce your cost by establishing:</p>
    <ul class="programs">
      <li>Pay-plan Management</li>
      <li>Pre-Collections</li>
      <li>Bad&nbsp; Debt</li>
    </ul>

    <div class="cta">
      <div class="cta-line">
        <svg class="cta-icon" viewBox="0 0 24 24" aria-hidden="true"><path d="M6.6 10.8a15.1 15.1 0 0 0 6.6 6.6l2.2-2.2c.3-.3.7-.4 1-.2 1.1.4 2.3.6 3.6.6.6 0 1 .4 1 1V20c0 .6-.4 1-1 1A17 17 0 0 1 3 4c0-.6.4-1 1-1h3.5c.6 0 1 .4 1 1 0 1.3.2 2.5.6 3.6.1.3 0 .7-.2 1z"/></svg>
        <span>Call us today</span>
      </div>
      <div class="cta-phone">800.555.0142</div>
    </div>

    <p class="footer-line">Receivable Management Solutions</p>
  </article>
</body>
</html>
```